Layout for site fence advertising - length approx. 250 cm x 125 cm

The advertising will later be printed on a PVC film and used for events or on sports fields.

Main services :
Your regional contact at
Real estate and business financing
independent insurance advice

```html
<!DOCTYPE html>
<html lang="en">
<head>
<meta charset="utf-8">
<title>Site fence advertising layout</title>
<link href="https://fonts.googleapis.com/css2?family=Montserrat:wght@500;600;700;800&family=Oswald:wght@600&display=swap" rel="stylesheet">
<style>
  :root {
    --sheet-grey: #c4c4c4;
    --brand-blue: #2a5caa;
    --brand-dark: #302a33;
    --band-grey: #3b3b3b;
    --text-grey: #5a5a5a;
    --white: #ffffff;
  }
  * { margin: 0; padding: 0; box-sizing: border-box; }
  html, body { width: 1080px; height: 1200px; overflow: hidden; }
  body {
    background: var(--sheet-grey);
    font-family: "Montserrat", Arial, sans-serif;
    color: #111;
    position: relative;
  }
  .sheet-title {
    position: absolute; top: 44px; left: 0; width: 1080px;
    text-align: center; font-size: 24px; font-weight: 500;
  }
  .sample-label {
    position: absolute; left: 95px; font-size: 17px; font-weight: 600;
  }
  .banner {
    position: absolute; left: 95px; width: 889px; height: 444px;
    background: var(--white); overflow: hidden;
    box-shadow: 0 2px 6px rgba(0,0,0,.35);
  }
  .banner-art { position: absolute; inset: 0; }
  .brand-mark {
    position: absolute; left: 43px; top: 34px; width: 112px; height: 112px;
    border: 4px solid var(--brand-blue); border-radius: 50%;
  }
  .brand-divider {
    position: absolute; left: 166px; top: 31px; width: 3px; height: 117px;
    background: var(--text-grey);
  }
  .brand-name {
    position: absolute; left: 177px; top: 63px;
    font-size: 19px; font-weight: 600; color: var(--brand-blue); white-space: nowrap;
  }
  .brand-tagline {
    position: absolute; left: 177px; top: 92px;
    font-size: 16.2px; font-weight: 500; color: var(--text-grey); white-space: nowrap;
  }
  .banner-text { position: absolute; left: 0; width: 532px; text-align: center; color: var(--white); white-space: nowrap; }
  .v1 .intro { top: 185px; font-size: 25px; font-weight: 500; left: 85px; width: 374px; }
  .v1 .headline {
    top: 234px; font-family: "Oswald", "Arial Narrow", sans-serif; font-weight: 600;
    font-size: 56px; line-height: 61px; letter-spacing: 0.5px;
  }
  .v1 .service { top: 384px; font-size: 29px; font-weight: 600; }
  .v2 .intro { top: 164px; font-size: 24px; font-weight: 600; color: var(--text-grey); }
  .v2 .headline { top: 211px; font-size: 40px; font-weight: 800; line-height: 45px; letter-spacing: -0.5px; }
  .v2 .service { top: 314px; font-size: 29px; font-weight: 600; }
  .v2 .call {
    top: 366px; font-size: 56px; font-weight: 800; letter-spacing: -2px;
    color: var(--brand-dark); text-align: center;
  }
  .v2 .call .number { color: var(--brand-blue); }
</style>
</head>
<body>
  <h1 class="sheet-title">Layout for site fence advertising - length approx. 250 cm x 125 cm</h1>

  <p class="sample-label" style="top:122px">Sample 1</p>
  <section class="banner v1" style="top:165px">
    <svg class="banner-art" width="889" height="444" viewBox="0 0 889 444">
      <defs>
        <linearGradient id="portrait-tone-1" x1="0" y1="0" x2="0" y2="1">
          <stop offset="0" stop-color="#f4ece8"/>
          <stop offset="0.55" stop-color="#e9d2c6"/>
          <stop offset="1" stop-color="#2b2a3a"/>
        </linearGradient>
      </defs>
      <rect x="0" y="177" width="620" height="194" fill="var(--brand-blue)"/>
      <polygon points="85,177 459,177 433,226 111,226" fill="var(--brand-dark)"/>
      <rect x="0" y="371" width="620" height="73" fill="var(--brand-dark)"/>
      <circle cx="735" cy="244" r="213" fill="var(--brand-blue)"/>
      <circle cx="735" cy="244" r="200" fill="var(--white)"/>
      <path role="img" aria-label="Portrait photo of the regional advisor in a dark suit and white shirt"
            d="M600 444 C640 330 700 290 700 190 C700 60 760 0 820 0 L889 0 L889 444 Z"
            fill="url(#portrait-tone-1)"/>
    </svg>
    <div class="brand-mark"></div>
    <div class="brand-divider"></div>
    <p class="brand-name">Nordlicht Finanzberatung GmbH</p>
    <p class="brand-tagline">Finanzieren, Versichern, Vorsorgen</p>
    <p class="banner-text intro">Your regional contact at</p>
    <h2 class="banner-text headline">REAL ESTATE AND<br>BUSINESS FINANCING</h2>
    <p class="banner-text service">Independent insurance advice</p>
  </section>

  <p class="sample-label" style="top:654px">Sample 2</p>
  <section class="banner v2" style="top:698px">
    <svg class="banner-art" width="889" height="444" viewBox="0 0 889 444">
      <defs>
        <linearGradient id="portrait-tone-2" x1="0" y1="0" x2="0" y2="1">
          <stop offset="0" stop-color="#f4ece8"/>
          <stop offset="0.55" stop-color="#e9d2c6"/>
          <stop offset="1" stop-color="#2b2a3a"/>
        </linearGradient>
      </defs>
      <rect x="0" y="202" width="620" height="107" fill="var(--brand-blue)"/>
      <rect x="0" y="309" width="620" height="47" fill="var(--band-grey)"/>
      <circle cx="735" cy="244" r="213" fill="var(--brand-blue)"/>
      <circle cx="735" cy="244" r="200" fill="var(--white)"/>
      <path role="img" aria-label="Portrait photo of the regional advisor in a dark suit and white shirt"
            d="M600 444 C640 330 700 290 700 190 C700 60 760 0 820 0 L889 0 L889 444 Z"
            fill="url(#portrait-tone-2)"/>
    </svg>
    <div class="brand-mark"></div>
    <div class="brand-divider"></div>
    <p class="brand-name">Nordlicht Finanzberatung GmbH</p>
    <p class="brand-tagline">Finanzieren, Versichern, Vorsorgen</p>
    <p class="banner-text intro">YOUR REGIONAL CONTACT AT</p>
    <h2 class="banner-text headline">REAL ESTATE AND<br>BUSINESS FINANCING</h2>
    <p class="banner-text service">Independent insurance advice</p>
    <p class="banner-text call">Call: <span class="number">0987.654.321</span></p>
  </section>
</body>
</html>
```